Sign listing benefits of Wash and Fold Service

Sign 48 inches wide and 24 inches height to showcase service listed above.
Benefits include:
Saves Money
Saves Time
Convenient
Stain Treatment

Looking for something colorful (Blue and white are our business colors) the look of a laundromat business.

```html
<!DOCTYPE html>
<html lang="en">
<head>
<meta charset="utf-8">
<title>Wash and Fold Benefits Sign</title>
<link rel="stylesheet" href="https://fonts.googleapis.com/css2?family=Montserrat:wght@400;900&display=swap">
<style>
  :root {
    --backdrop: #07121f;
    --sky: #6dd3e3;
    --foam: #ffffff;
    --navy: #14306a;
    --teal: #1d8c9d;
    --teal-label: #1a93a4;
  }
  html, body {
    margin: 0;
    padding: 0;
    width: 1200px;
    height: 1200px;
    overflow: hidden;
    background: var(--backdrop);
  }
  .sign {
    position: absolute;
    left: 71px;
    top: 311px;
    width: 1056px;
    height: 528px;
    overflow: hidden;
    font-family: "Montserrat", Arial, sans-serif;
  }
  .sign-art {
    position: absolute;
    inset: 0;
  }
  .name-pill {
    position: absolute;
    left: 211px;
    top: 37px;
    width: 624px;
    height: 72px;
    border-radius: 36px;
    background: var(--foam);
    display: flex;
    align-items: center;
    justify-content: center;
    color: var(--teal);
    font-weight: 400;
    font-size: 41px;
    letter-spacing: 2px;
  }
  .benefit-label {
    position: absolute;
    top: 443px;
    width: 260px;
    margin-left: -130px;
    text-align: center;
    color: var(--teal-label);
    font-weight: 900;
    font-size: 27px;
    line-height: 30px;
    letter-spacing: 0.3px;
    text-transform: uppercase;
  }
</style>
</head>
<body>
  <div class="sign">
    <svg class="sign-art" width="1056" height="528" viewBox="0 0 1056 528">
      <defs>
        <linearGradient id="sky-fill" x1="0" y1="0" x2="0" y2="1">
          <stop offset="0" stop-color="#6dd3e3"/>
          <stop offset="0.6" stop-color="#86dbe8"/>
          <stop offset="1" stop-color="#b9ebf2"/>
        </linearGradient>
        <linearGradient id="foam-fill" x1="0" y1="0" x2="0" y2="1">
          <stop offset="0" stop-color="#e6f7fa"/>
          <stop offset="0.5" stop-color="#ffffff"/>
        </linearGradient>
        <linearGradient id="silver-ring" x1="0" y1="0" x2="1" y2="1">
          <stop offset="0" stop-color="#f4f6f8"/>
          <stop offset="0.5" stop-color="#c3c9d0"/>
          <stop offset="1" stop-color="#8e98a3"/>
        </linearGradient>
        <radialGradient id="icon-field" cx="0.5" cy="0.5" r="0.5">
          <stop offset="0" stop-color="#d6f2f7"/>
          <stop offset="1" stop-color="#a9e3ed"/>
        </radialGradient>
      </defs>

      <g class="soap-backdrop" role="img" aria-label="Soap bubbles and foam background">
        <rect width="1056" height="528" fill="url(#sky-fill)"/>
        <path class="foam-band" fill="url(#foam-fill)"
          d="M0 300 Q40 270 80 292 Q120 262 170 286 Q220 258 270 284 Q320 262 372 288 Q420 264 470 290 Q520 262 575 288 Q625 266 675 290 Q725 262 778 286 Q828 264 880 290 Q930 262 985 284 Q1025 268 1056 288 L1056 528 L0 528 Z"/>
        <path class="foam-crest" fill="#ffffff"
          d="M0 360 Q60 330 120 352 Q190 326 260 350 Q330 328 400 352 Q470 326 540 350 Q610 328 680 352 Q750 326 820 350 Q890 328 960 352 Q1010 334 1056 348 L1056 528 L0 528 Z"/>
      </g>

      <g class="benefit-badge badge-money">
        <circle cx="143" cy="316" r="108" fill="#ffffff"/>
        <circle cx="143" cy="316" r="96" fill="none" stroke="#14306a" stroke-width="18"/>
        <circle cx="143" cy="316" r="80" fill="url(#silver-ring)"/>
        <circle cx="143" cy="316" r="68" fill="#ffffff"/>
        <circle cx="143" cy="316" r="62" fill="url(#icon-field)"/>
        <g class="icon-money" fill="#1d8c9d">
          <circle cx="143" cy="282" r="16"/>
          <text x="143" y="290" text-anchor="middle" font-family="Montserrat, Arial, sans-serif" font-weight="900" font-size="21" fill="#ffffff">$</text>
          <path d="M137 302 h12 v10 h9 l-15 14 l-15 -14 h9 Z"/>
          <rect x="108" y="330" width="70" height="28" rx="8"/>
          <rect x="126" y="336" width="34" height="5" rx="2.5" fill="#ffffff"/>
        </g>
      </g>

      <g class="benefit-badge badge-time">
        <circle cx="400" cy="316" r="108" fill="#ffffff"/>
        <circle cx="400" cy="316" r="96" fill="none" stroke="#14306a" stroke-width="18"/>
        <circle cx="400" cy="316" r="80" fill="url(#silver-ring)"/>
        <circle cx="400" cy="316" r="68" fill="#ffffff"/>
        <circle cx="400" cy="316" r="62" fill="url(#icon-field)"/>
        <g class="icon-clock">
          <circle cx="410" cy="296" r="22" fill="#ffffff" stroke="#1d8c9d" stroke-width="6"/>
          <path d="M410 283 V297 H420" fill="none" stroke="#1d8c9d" stroke-width="4" stroke-linecap="round"/>
          <rect x="356" y="326" width="14" height="30" rx="2" fill="#1d8c9d"/>
          <path d="M374 330 H410 Q420 330 420 338 L444 326 Q452 322 454 330 L420 352 H374 Z" fill="#1d8c9d"/>
        </g>
      </g>

      <g class="benefit-badge badge-convenient">
        <circle cx="659" cy="316" r="108" fill="#ffffff"/>
        <circle cx="659" cy="316" r="96" fill="none" stroke="#14306a" stroke-width="18"/>
        <circle cx="659" cy="316" r="80" fill="url(#silver-ring)"/>
        <circle cx="659" cy="316" r="68" fill="#ffffff"/>
        <circle cx="659" cy="316" r="62" fill="url(#icon-field)"/>
        <circle cx="659" cy="316" r="44" fill="#1d8c9d" role="img" aria-label="Icon: smiling emoji"/>
      </g>

      <g class="benefit-badge badge-stain">
        <circle cx="916" cy="316" r="108" fill="#ffffff"/>
        <circle cx="916" cy="316" r="96" fill="none" stroke="#14306a" stroke-width="18"/>
        <circle cx="916" cy="316" r="80" fill="url(#silver-ring)"/>
        <circle cx="916" cy="316" r="68" fill="#ffffff"/>
        <circle cx="916" cy="316" r="62" fill="url(#icon-field)"/>
        <g class="icon-sparkles" fill="#1d8c9d">
          <path d="M898 268 Q902 290 922 294 Q902 298 898 320 Q894 298 874 294 Q894 290 898 268 Z"/>
          <path d="M940 292 Q943 308 956 311 Q943 314 940 330 Q937 314 924 311 Q937 308 940 292 Z"/>
          <path d="M884 326 Q886 336 895 338 Q886 340 884 350 Q882 340 873 338 Q882 336 884 326 Z"/>
          <path d="M922 334 Q924 344 933 346 Q924 348 922 358 Q920 348 911 346 Q920 344 922 334 Z"/>
        </g>
      </g>
    </svg>

    <div class="name-pill">LAUNDROMAT NAME</div>

    <div class="benefit-label" style="left:143px">Saves<br>Money</div>
    <div class="benefit-label" style="left:400px">Saves<br>Time</div>
    <div class="benefit-label" style="left:659px">Convenient</div>
    <div class="benefit-label" style="left:916px">Stain<br>Treatment</div>
  </div>
</body>
</html>
```